Introduction of new dentist and new treatments

We want inform our Patients of our new dentist and new treatment methods. It is dealing about biologic dentistry and holistic dentistry. we are in switzerland and speak german

Font styles to use
Sans Serif

Colors
00a990
33b8a4
9bcb3c
acd036
cadf82
0292cd
3176b5
e34297
e667a6

Requirements
Must have
• Text, which can be edited. It will be in german
• Name of the dental clinic is
• "Velmora - Ihr Zahnarzt in Zug"
Nice to have
• A4 Layout

```html
<!DOCTYPE html>
<html lang="de">
<head>
<meta charset="utf-8">
<title>Velmora – Interdisziplinäre Zahnmedizin</title>
<link rel="stylesheet" href="https://fonts.googleapis.com/css2?family=Roboto+Condensed:wght@700&family=Hind:wght@400;600&family=Cinzel:wght@500&display=swap">
<style>
  :root{
    --backdrop:#e9ebee;
    --paper:#f4f8fc;
    --sky-light:#dcebf8;
    --sky:#9cc8ec;
    --blue:#2a73b8;
    --blue-deep:#1f63ad;
    --navy:#253449;
    --pink:#d6367f;
    --teal-line:#a9d3da;
    --ink:#222428;
    --footer-a:#4a9ad8;
    --footer-b:#2a73c0;
  }
  *{box-sizing:border-box;margin:0;padding:0}
  html,body{width:1200px;height:1200px;overflow:hidden}
  body{background:var(--backdrop);position:relative;font-family:"Hind",sans-serif}
  .flyer{position:absolute;left:180px;top:35px;width:840px;height:1130px;background:var(--paper);overflow:hidden;box-shadow:0 6px 24px rgba(0,0,0,.18)}
  .header-art{position:absolute;left:0;top:0;width:840px;height:310px}
  .portrait{position:absolute;left:528px;top:14px;width:312px;height:284px}
  .brand{position:absolute;left:230px;top:150px;width:340px;text-align:center}
  .brand-name{font-family:"Cinzel",serif;font-weight:500;font-size:25px;letter-spacing:6px;color:var(--navy);display:flex;align-items:center;justify-content:center;gap:10px}
  .brand-dot{width:10px;height:10px;border-radius:50%;background:var(--blue)}
  .brand-tag{font-size:12px;color:var(--navy);margin-top:2px;font-weight:600}
  .content{position:absolute;left:69px;top:322px;width:703px;color:var(--ink)}
  .title{font-family:"Roboto Condensed",sans-serif;font-weight:700;font-size:35px;color:var(--blue);line-height:1.1}
  .subtitle{font-family:"Roboto Condensed",sans-serif;font-weight:700;font-size:21px;color:var(--ink);margin-top:5px;letter-spacing:.1px}
  .intro,.section p{font-size:14px;line-height:20.5px;text-align:justify}
  .intro{margin-top:22px}
  .section{margin-top:20px}
  .section h2{font-size:14px;font-weight:600;color:var(--blue-deep);line-height:20.5px}
  .footer-art{position:absolute;left:0;bottom:0;width:840px;height:80px}
  .call{position:absolute;left:69px;bottom:14px;color:#fff;font-family:"Roboto Condensed",sans-serif;font-size:20px;font-weight:400}
  .call strong{font-size:27px;font-weight:700;letter-spacing:.5px;margin-left:4px}
</style>
</head>
<body>
<main class="flyer">
  <svg class="header-art" viewBox="0 0 840 310" aria-hidden="true">
    <defs>
      <linearGradient id="sky" x1="0" y1="0" x2="1" y2="1">
        <stop offset="0" stop-color="#e6f1fb"/>
        <stop offset=".6" stop-color="#b9dbf4"/>
        <stop offset="1" stop-color="#8cc3ec"/>
      </linearGradient>
    </defs>
    <path d="M0 0H840V276C600 310 300 300 0 122Z" fill="url(#sky)"/>
    <path d="M0 150C260 290 560 310 840 280" fill="none" stroke="var(--teal-line)" stroke-width="5"/>
    <path d="M0 124C260 288 560 305 840 276" fill="none" stroke="var(--pink)" stroke-width="8"/>
  </svg>
  <div class="portrait" role="img" aria-label="Porträtfoto des neuen Zahnarztes im blauen Poloshirt" style="background:linear-gradient(180deg,#d9b7a3 0%,#c99d86 55%,#2f6fb8 70%,#245fa6 100%);border-radius:140px 140px 0 0;opacity:.9;clip-path:polygon(0 100%,8% 82%,30% 70%,30% 0,75% 0,75% 70%,95% 78%,100% 100%)"></div>
  <div class="brand">
    <div class="brand-name"><span class="brand-dot"></span>VELMORA</div>
    <div class="brand-tag">Ihr Zahnarzt in Zug</div>
  </div>

  <section class="content">
    <h1 class="title">Interdisziplinäre Zahnmedizin</h1>
    <p class="subtitle">Zusammenhang zwischen Zahnproblemen und der Gesundheit von Körper und Geist</p>
    <p class="intro">Zahn und Gesundheit haben eins gemeinsam – Man vermisst sie, wenn sie fehlt. Zähne haben einen engen Zusammenhang zur Gesundheit und können diese beeinflussen. Sowohl negativ als auch positiv.</p>

    <div class="section">
      <h2>Funktion des Kauorgans und interdisziplinäre Zahnmedizin</h2>
      <p>„Funktion ist nicht alles. Aber ohne Funktion ist alles nichts!“ Sagte einst Prof.A.Lindqvist(Zahnarzt, Gnathologie) und betonte die Bedeutung der Funktion des Kausystems. Sprechen, Kauen aber auch Körperhaltung und Stressmanagement gehören zu den Funktionen der Zähne. Ein gut funktionierendes Kauorgan (nach Prof.R. Halberg, interdisziplinäre Zahnmedizin) kann Stress bewältigen und mehr Leistung und Wohlbefinden bringen. Sehr oft erkennt man Funktionsstörungen daran, dass die Zähne nicht richtig zueinander passen oder Muskelverspannungen und Schmerzen im Kiefergelenk auftreten.</p>
    </div>

    <div class="section">
      <h2>Parodontitis und systemische Erkrankungen</h2>
      <p>Parodontitis (Entzündung des Zahnhalteapparats) ist eine der häufigsten chronischen Krankheiten weltweit und daher gut erforscht. Herzkrankheiten, Diabetes und Frühgeburtlichkeit sind einige der systemischen Krankheiten mit der Parodontitis in Zusammenhang steht. Zahnfleischbulten, Zahnlockerung, Zahnfleischschwund und Zahnverlust sind typische Begleiterscheinungen von Parodontitis. Eine systematische Parodontitis-Behandlung kann auch positive Auswirkungen auf die gesamte Gesundheit haben.</p>
    </div>

    <div class="section">
      <h2>Zahnverlust und neurologische Auswirkung</h2>
      <p>Ein physiologisches Kausystem hat sehr feine Steuerungs- und Wahrnehmungsmöglichkeiten. Bei Zahnverlust werden diese Fähigkeiten weniger benötigt. Weniger gebrauchte Ressourcen werden von der Natur dementsprechend abgebaut. Studien zeigen, dass Menschen mit weniger Zähnen mehr Risiko zur Bildung von Demenz bergen.</p>
    </div>

    <div class="section">
      <h2>Ganzheitliche Erklärungen</h2>
      <p>Die komplementäre Zahnheilkunde, sehr oft auch als ganzheitliche oder biologische Zahnheilkunde bezeichnet, versucht mit Hilfe von Meridianen(Traditionelle Chinesische Medizin), den Zusammenhang zwischen Zähnen und anderen Organen und Körperteilen zu erklären. Es gibt immer mehr Patienten und Zahnärzte die von dieser Theorie und deren Ergebnissen überzeugt sind. Aufgrund der wissenschaftlichen Lage ist eine ausführliche Aufklärung vor der Behandlung sehr ratsam.</p>
    </div>
  </section>

  <svg class="footer-art" viewBox="0 0 840 80" aria-hidden="true">
    <defs>
      <linearGradient id="band" x1="0" y1="0" x2="1" y2="0">
        <stop offset="0" stop-color="var(--footer-b)"/>
        <stop offset="1" stop-color="var(--footer-a)"/>
      </linearGradient>
    </defs>
    <path d="M0 16C250 -4 480 10 660 80H0Z" fill="url(#band)"/>
    <path d="M0 12C250 -8 490 8 680 80" fill="none" stroke="var(--pink)" stroke-width="6"/>
    <path d="M0 6C260 -12 500 4 700 80" fill="none" stroke="var(--teal-line)" stroke-width="3"/>
  </svg>
  <p class="call">Call: <strong>+41 41 555 12 34</strong></p>
</main>
</body>
</html>
```